Business Card for Financial Asset Management Company

Now we are launching a new company based in Tokyo.
The company information is below;

Company Name: Caldera Stewardship

Operations: Financial assets management, Proposing forming portfolio of assets, Consulting service, and advising to enhance your company's financial health

Corporate Colour: Japan Blue or Navy like below
http://pages.art.velmoreu.edu/tkovan/images/Indigo/Aqua-Indigo-104.jpg

It's dark and deep, and will get to fit to our clients as our relationships last longer and longer.

Our images for this colour are "Japanese style" and "pride in our craftmanship" , and also "gentle".

Corporate Key Image: an order taker who is sincere, polite, but courageous

We don't have our logo yet so please feel free to put any symbol on your design.

Please do not hesitate about asking any questions.
Thank you :-)

Reason: We are still discussin on final decision. Thank you for your understanding.

```html
<!DOCTYPE html>
<html lang="en">
<head>
<meta charset="utf-8">
<title>Caldera Stewardship — Business Card</title>
<link rel="stylesheet" href="https://fonts.googleapis.com/css2?family=Source+Sans+3:wght@400;600;700&display=swap">
<style>
  :root {
    --backdrop: #aeadae;
    --indigo-deep: #16122e;
    --indigo: #2e2766;
    --indigo-bright: #3a3189;
    --paper: #ffffff;
    --ink: #1a1a1a;
    --rule: #555555;
  }
  * { margin: 0; padding: 0; box-sizing: border-box; }
  html, body { width: 1200px; height: 900px; overflow: hidden; }
  body {
    position: relative;
    background: var(--backdrop);
    font-family: "Source Sans 3", Arial, sans-serif;
  }
  .card {
    position: absolute;
    top: 229px;
    width: 566px;
    height: 328px;
    border-radius: 24px;
    overflow: hidden;
    box-shadow: 3px 4px 6px rgba(0,0,0,0.45);
  }
  .card--front { left: 28px; }
  .card--back { left: 612px; background: var(--paper); }

  .front-texture {
    position: absolute; inset: 0;
    background:
      radial-gradient(ellipse 60% 55% at 55% 25%, rgba(80,68,170,0.55), transparent 70%),
      linear-gradient(170deg, var(--indigo-bright) 0%, var(--indigo) 45%, var(--indigo-deep) 100%);
  }

  .brand { position: absolute; display: flex; align-items: center; }
  .brand__mark { flex: none; border-radius: 50%; }
  .brand__rule { flex: none; width: 1.5px; }
  .brand__name { font-weight: 700; line-height: 0.93; letter-spacing: -0.3px; }

  .card--front .brand { left: 69px; top: 101px; }
  .card--front .brand__mark { width: 76px; height: 76px; border: 3px solid var(--paper); margin-right: 82px; }
  .card--front .brand__rule { height: 122px; background: var(--paper); margin-right: 20px; }
  .card--front .brand__name { color: var(--paper); font-size: 41px; }

  .card--back .brand { left: 36px; top: 34px; }
  .card--back .brand__mark { width: 74px; height: 74px; border: 3px solid var(--indigo); margin-right: 31px; }
  .card--back .brand__rule { height: 88px; background: var(--rule); margin-right: 14px; }
  .card--back .brand__name { color: var(--indigo); font-size: 28px; }

  .address {
    position: absolute; left: 37px; top: 132px;
    font-size: 16.5px; line-height: 21px; color: var(--ink);
  }
  .contacts {
    position: absolute; left: 36px; top: 209px;
    list-style: none; font-size: 16.5px; line-height: 17px; color: var(--ink);
  }
  .contacts li { display: flex; align-items: center; height: 17px; }
  .contacts svg, .contacts .fx { width: 14px; margin-right: 13px; flex: none; }
  .contacts .fx { font-size: 12px; color: var(--indigo); }

  .nameplate {
    position: absolute; left: 377px; top: 213px;
    width: 189px; height: 62px;
    background: var(--indigo); color: var(--paper);
    text-align: right; padding: 5px 28px 0 0;
  }
  .nameplate__name { font-size: 21px; line-height: 25px; }
  .nameplate__title { font-size: 16.5px; line-height: 20px; }
</style>
</head>
<body>

<section class="card card--front">
  <div class="front-texture" role="img" aria-label="Soft flowing indigo light ribbons across a deep navy field"></div>
  <div class="brand">
    <span class="brand__mark"></span>
    <span class="brand__rule"></span>
    <span class="brand__name">Caldera<br>Stewardship</span>
  </div>
</section>

<section class="card card--back">
  <div class="brand">
    <span class="brand__mark"></span>
    <span class="brand__rule"></span>
    <span class="brand__name">Caldera<br>Stewardship</span>
  </div>

  <p class="address">Your address can put here<br>Your address can put here</p>

  <ul class="contacts">
    <li>
      <svg viewBox="0 0 14 10" height="10"><path fill="#2e2766" d="M1 3c0-2 12-2 12 0v1h-3V3H4v1H1zM3 5h8l1 4H2z"/></svg>
      0123 456 789
    </li>
    <li>
      <svg viewBox="0 0 14 12" height="12"><rect x="3" y="0.5" width="8" height="11" rx="1" fill="none" stroke="#2e2766" stroke-width="1.2"/></svg>
      0123 456 789
    </li>
    <li><span class="fx">Fx</span>0123 456 789</li>
    <li>
      <svg viewBox="0 0 14 9" height="9"><rect x="1" y="0.5" width="11" height="8" fill="#2e2766"/><path d="M1 1l5.5 4L12 1" fill="none" stroke="#fff" stroke-width="1"/></svg>
      youremail@mail.com
    </li>
  </ul>

  <div class="nameplate">
    <p class="nameplate__name">Mika Sorano</p>
    <p class="nameplate__title">Your title here</p>
  </div>
</section>

</body>
</html>
```